Using attached logo that has been created

Business card with logo that's attached. Maybe with water or the cartoon van in background. Looking for it to not be so plain and not too white.
Information to include;
Rudy Castell
(619) 555-0187
Info@brenwickpipeworks.us
www.brenwickpipeworks.us
License # 4720519
Looking forward to the designs u come up with.
Thank you!
-Delia
Updates
The designer (Tessa), that I would like to work with requested an extension to allow time to create a couple designs for this project.
Target Market(s)
Plumbing
Industry/Entity Type
Plumbing
Contact Information for Business Card
Listed above

```html
<!DOCTYPE html>
<html lang="en">
<head>
<meta charset="utf-8">
<title>Brenwick Pipeworks — Business Card</title>
<link rel="stylesheet" href="https://fonts.googleapis.com/css2?family=Poppins:wght@400;600;800&family=Playball&family=Cutive+Mono&display=swap">
<style>
  :root {
    --stage: #2b2b2d;
    --sun: #ffc20e;
    --sun-soft: #ffd24d;
    --royal: #1156a8;
    --ink: #1d1d1f;
    --paper: #ffffff;
    --mist: #e6ebf3;
    --mist-deep: #c9d4e6;
  }
  * { box-sizing: border-box; margin: 0; padding: 0; }
  html, body { width: 1200px; height: 874px; overflow: hidden; }
  body {
    background: var(--stage);
    font-family: "Poppins", sans-serif;
    position: relative;
  }
  .card {
    position: absolute;
    width: 620px;
    height: 355px;
    border-radius: 22px;
    overflow: hidden;
    box-shadow: 0 18px 40px rgba(0,0,0,.45);
  }

  /* Front */
  .card--front { left: 440px; top: 48px; background: var(--sun); }
  .front__art {
    position: absolute; left: 230px; top: 34px; width: 160px; height: 172px;
    border-radius: 12px;
    background: linear-gradient(180deg, var(--sun-soft) 0%, var(--sun) 100%);
  }
  .front__brand {
    position: absolute; left: 0; right: 0; top: 224px; text-align: center;
    font-weight: 800; font-size: 30px; line-height: 1.1; color: var(--royal); letter-spacing: 1px;
  }
  .front__brand-sub {
    position: absolute; left: 0; right: 0; top: 264px; text-align: center;
    font-weight: 800; font-size: 13px; color: var(--royal); letter-spacing: 3px;
  }
  .front__web {
    position: absolute; left: 0; right: 0; bottom: 36px; text-align: center;
    font-family: "Cutive Mono", monospace; font-size: 17px; letter-spacing: 6px; color: var(--ink);
  }

  /* Back */
  .card--back { left: 180px; top: 450px; background: var(--paper); }
  .back__swoosh { position: absolute; inset: 0; }
  .back__art {
    position: absolute; right: 70px; top: 60px; width: 210px; height: 295px;
    border-radius: 12px 12px 0 0;
    background: linear-gradient(180deg, var(--mist) 0%, var(--mist-deep) 100%);
  }
  .back__details {
    position: absolute; left: 38px; top: 172px; color: var(--paper);
  }
  .back__name {
    font-family: "Playball", cursive; font-size: 34px; line-height: 1.1; margin-bottom: 10px;
  }
  .back__line { font-size: 15px; line-height: 1.45; }
</style>
</head>
<body>

  <section class="card card--front" aria-label="Card front">
    <div class="front__art" role="img" aria-label="Mascot illustration area"></div>
    <div class="front__brand">BRENWICK PIPEWORKS</div>
    <div class="front__brand-sub">&amp; MORE</div>
    <div class="front__web">WWW.BRENWICKPIPEWORKS.US</div>
  </section>

  <section class="card card--back" aria-label="Card back">
    <svg class="back__swoosh" viewBox="0 0 620 355" preserveAspectRatio="none" aria-hidden="true">
      <path d="M0,0 L160,0 C250,70 270,170 340,235 C390,285 430,320 452,355 L0,355 Z" fill="var(--sun)"/>
      <path d="M0,0 L140,0 C230,75 250,175 320,240 C370,290 410,322 430,355 L0,355 Z" fill="var(--ink)"/>
      <path d="M0,0 L136,0 C226,76 246,176 316,241 C366,291 405,323 425,355 L0,355 Z" fill="var(--royal)"/>
    </svg>
    <div class="back__art" role="img" aria-label="Mascot illustration area"></div>
    <div class="back__details">
      <p class="back__name">Rudy Castell</p>
      <p class="back__line">P. (619) 555-0187</p>
      <p class="back__line">Info@brenwickpipeworks.us</p>
      <p class="back__line">www.brenwickpipeworks.us</p>
      <p class="back__line">License # 4720519</p>
    </div>
  </section>

</body>
</html>
```